Belmora Wines

Hi all,

My name’s Liam Dowsett and I run a small wine brand based in the Canberra Wine District, Australia. I’m currently in the process of branding the business and am looking for a designer to help develop a new visual direction.

Background
I’ll be growing my own fruit from a leased vineyard site Named 'Wrenhollow' and my family’s property named 'Tibbard Vale', with a stronger emphasis on organic practices and site expression.

The Direction
The brand will centre around single vineyard wines, with each wine reflecting the unique site it comes from. I’d like the branding to support this idea of place, origin, and authenticity.

In terms of visual style, I’m drawn to something that is:

Simple and effective
A balance between traditional and modern
Clean, considered, and not overly decorative

Nothing too over-the-top, the goal is something timeless that lets the wine and vineyard story speak for itself.

At this stage, I’m mainly looking for:

Conceptual design direction / ideas
Label design (with potential to expand into broader branding)

I’m open to creative interpretation, so if the story resonates with you, I’d love to see how you would approach it.

Below I've attached an example of the bottle shape I will be using.

Cheers,
Liam

Colors
0054AA
0677BA
7BADD7
CADEEF
E8F1F8
FFC000
F8CF3A
FAE287
FDF2CF
FEFAEE

Requirements
Must have
• Mix of modern and traditional

```html
<!DOCTYPE html>
<html lang="en">
<head>
<meta charset="utf-8">
<title>Wrenhollow Riesling Label</title>
<link href="https://fonts.googleapis.com/css2?family=Playfair+Display:wght@500;600;700&display=swap" rel="stylesheet">
<style>
  :root {
    --backdrop: #e4e5e6;
    --label-light: #e8eef3;
    --label-mid: #d3dee6;
    --label-deep: #b9c7d1;
    --foil: #c9ced2;
    --foil-shine: #f2f4f5;
    --ink: #111418;
    --art-yellow: #f8cf3a;
    --art-blue: #7badd7;
    --art-pale: #e8f1f8;
  }
  * { margin: 0; padding: 0; box-sizing: border-box; }
  html, body {
    width: 1200px;
    height: 1200px;
    overflow: hidden;
    background: var(--backdrop);
  }
  .canvas {
    position: relative;
    width: 1200px;
    height: 1200px;
    display: flex;
    align-items: center;
    justify-content: center;
  }
  .label {
    position: relative;
    width: 800px;
    height: 1080px;
    background: linear-gradient(90deg, var(--label-light) 0%, var(--label-mid) 55%, var(--label-deep) 100%);
    color: var(--ink);
    font-family: "Playfair Display", Georgia, serif;
    box-shadow: 0 10px 30px rgba(0,0,0,0.08);
  }
  .label__foil {
    position: absolute;
    left: 0;
    width: 100%;
    height: 14px;
    background: linear-gradient(180deg, var(--foil-shine), var(--foil));
  }
  .label__foil--top { top: 0; }
  .label__foil--bottom { bottom: 0; }
  .brand-name {
    position: absolute;
    top: 88px;
    left: 0;
    width: 100%;
    text-align: center;
    font-size: 76px;
    font-weight: 600;
    letter-spacing: 0.32em;
    padding-left: 0.32em;
    line-height: 1;
  }
  .vineyard-name {
    position: absolute;
    top: 262px;
    right: 40px;
    width: 150px;
    text-align: right;
    font-size: 26px;
    font-weight: 600;
    line-height: 1.25;
  }
  .illustration {
    position: absolute;
    left: 60px;
    top: 232px;
    width: 510px;
    height: 700px;
    border-radius: 48% 52% 40% 44% / 38% 40% 30% 30%;
    background:
      radial-gradient(ellipse at 55% 50%, var(--art-yellow) 0%, rgba(248,207,58,0.85) 30%, rgba(248,207,58,0) 55%),
      radial-gradient(ellipse at 40% 85%, var(--art-pale) 0%, rgba(232,241,248,0) 60%),
      radial-gradient(ellipse at 20% 15%, var(--art-blue) 0%, rgba(123,173,215,0) 35%);
  }
  .varietal {
    position: absolute;
    left: 705px;
    top: 738px;
    transform: translate(-50%, -50%) rotate(-90deg);
    font-size: 46px;
    font-weight: 700;
    letter-spacing: 0.3em;
    white-space: nowrap;
    line-height: 1;
  }
  .label__footer {
    position: absolute;
    left: 52px;
    right: 30px;
    bottom: 40px;
    display: flex;
    justify-content: space-between;
    font-size: 26px;
    font-weight: 600;
  }
</style>
</head>
<body>
  <main class="canvas">
    <article class="label">
      <div class="label__foil label__foil--top"></div>
      <h1 class="brand-name">Wrenhollow</h1>
      <p class="vineyard-name">Tibbard<br>Vale<br>Vineyard</p>
      <div class="illustration" role="img" aria-label="Line illustration of a seated fox in yellow and blue with soft abstract shapes"></div>
      <p class="varietal">Riesling</p>
      <footer class="label__footer">
        <span class="abv">11.5% ALC/VOL</span>
        <span class="volume">750 ml</span>
      </footer>
      <div class="label__foil label__foil--bottom"></div>
    </article>
  </main>
</body>
</html>
```